Varrowick Biomedical Research Institute (VBRI) Web Design

VBRI is a non-profit organization focused on saving the lives of terminally ill patients by becoming the leaders in cutting-edge research, innovative technologies, utilizing national and international partnerships as well as the associated allopathic and naturopathic treatments necessary to do so.

Our primary focus is raising funds to support the research and acquisition of new technologies for life saving treatments which are NOT a one size fits all approach like conventional medicine but rather a marriage of the latest technologies used in combination with other new treatment possibilities for a successful end result.

Our domain is varrowickbr.org

Logo files are attached.

Looking for something clean, light, healthy.

Target Market(s)

The site should look and feel towards research/scientific grant writing.
Medical professionals, Medical Scientists.

Industry/Entity Type

Medical And Science

Number of Pages Required

4 page

Requirements
Nice to have
• Here are examples of sites I like in the order of how much I like them.
• https://www.palvenhope.org/give.html
• https://www.thekqtf.org/donate-to-kqtf
• https://www.curewaveinst.org/we-are-cwi/join-the-cause
• https://www.healquest.org/involved/donate.html
• https://give.nptf.org/checkout/donation?eid=58217
• https://www.moravind.org/how-you-can-help
• https://donate3.healquest.org/

```html
<!DOCTYPE html>
<html lang="en">
<head>
<meta charset="utf-8">
<title>Varrowick Biomedical Research Institute</title>
<link href="https://fonts.googleapis.com/css2?family=Open+Sans:wght@400;600;700;800&display=swap" rel="stylesheet">
<style>
:root{
  --blue:#1b6fb4;
  --green:#79b543;
  --green-panel:rgba(122,182,72,.92);
  --text:#333;
  --muted:#666;
  --white:#fff;
}
*{margin:0;padding:0;box-sizing:border-box}
html,body{width:1200px;height:3114px;overflow:hidden}
body{font-family:"Open Sans",Arial,sans-serif;color:var(--text);background:var(--white);position:relative}
.abs{position:absolute}
a{color:inherit;text-decoration:none}

/* header */
.site-header{position:absolute;left:0;top:0;width:1200px;height:115px;background:var(--white)}
.brand{position:absolute;left:135px;top:28px;display:flex;align-items:center;gap:12px}
.brand-mark{width:44px;height:44px;border-radius:50%;background:var(--green);flex:none}
.brand-name{font-size:16px;font-weight:700;color:var(--blue);line-height:1.2;width:200px}
.call{position:absolute;left:733px;top:28px;display:flex;align-items:center;gap:10px}
.call-icon{width:30px;height:30px;border-radius:50%;background:var(--green);display:flex;align-items:center;justify-content:center}
.call-label{font-size:10px;font-weight:700;color:#222;line-height:1}
.call-number{font-size:19px;font-weight:700;color:var(--blue);line-height:1.2}
.search{position:absolute;left:930px;top:26px;width:138px;height:32px;border:1px solid #ccc;font-size:10px;color:#444;padding:9px 10px}
.search svg{position:absolute;right:9px;top:10px}
.main-nav{position:absolute;left:512px;top:84px;display:flex;gap:27px;font-size:11px;font-weight:600;color:#222}
.main-nav .active{color:var(--green)}

/* hero */
.hero{position:absolute;left:0;top:115px;width:1200px;height:520px;background:linear-gradient(100deg,#d7e4ee 0%,#aac3d9 30%,#7fa3c4 55%,#c6d7e6 80%,#e6eef5 100%)}
.hero-title{position:absolute;left:0;top:293px;width:1200px;text-align:center;color:var(--white);font-size:38px;font-weight:800;line-height:1.15;text-shadow:0 2px 6px rgba(0,0,0,.25)}
.btn{display:inline-block;font-size:14px;font-weight:700;color:var(--white);text-align:center;text-transform:uppercase}
.btn-blue{background:var(--blue)}
.btn-green{background:var(--green)}
.hero .btn{position:absolute;left:532px;top:414px;width:136px;height:38px;line-height:38px}
.hero-arrow{position:absolute;top:240px}

/* section headings */
.sec-title{position:absolute;left:0;width:1200px;text-align:center;font-size:19px;font-weight:700;color:var(--blue)}
.sec-rule{position:absolute;left:573px;width:54px;height:3px;background:var(--green)}

/* services */
.service{position:absolute;top:765px;width:230px;text-align:center}
.service-icon{width:98px;height:98px;border:2px solid var(--green);border-radius:50%;margin:0 auto;display:flex;align-items:center;justify-content:center}
.service h3{font-size:13px;font-weight:400;color:#222;margin-top:33px}
.service p{font-size:10.5px;color:var(--muted);line-height:1.55;margin:14px auto 0;width:185px}

/* welcome */
.welcome{position:absolute;left:0;top:1045px;width:1200px;height:460px;background:linear-gradient(90deg,#3d82bd 0%,#2a78bb 40%,#1d6fb5 70%,#5d98c8 100%)}
.welcome .sec-title{color:var(--white)}
.welcome-text{position:absolute;left:360px;top:136px;width:480px;text-align:center;color:var(--white);font-size:12.5px;line-height:1.75}
.feature{position:absolute;top:232px;width:231px;height:161px;background:rgba(225,236,245,.9);text-align:center;padding-top:22px}
.feature h4{font-size:13px;font-weight:700;color:var(--blue);margin-top:10px}
.feature p{font-size:11px;color:#555;line-height:1.5;margin:8px 26px 0}
.welcome .btn{position:absolute;left:532px;top:437px;width:136px;height:38px;line-height:38px}

/* blog */
.post{position:absolute;top:1665px;width:295px}
.post-img{width:295px;height:210px}
.post-body{width:275px;height:93px;background:#f0f0f0;padding:14px 22px}
.post-body h4{font-size:12px;font-weight:700;color:#222;line-height:1.35}
.post-body p{font-size:10.5px;color:var(--muted);line-height:1.5;margin-top:8px;width:185px}

/* leadership */
.leadership{position:absolute;left:0;top:2039px;width:1200px;height:458px;background:linear-gradient(90deg,#dfe6ea 0%,#cfd9e0 45%,#b8c6d2 70%,#dde4ea 100%)}
.lead-panel{position:absolute;left:135px;top:0;width:425px;height:458px;background:var(--green-panel);padding:52px 64px 0 65px;color:var(--white)}
.lead-panel h3{font-size:17px;font-weight:700}
.lead-panel p{font-size:12.5px;line-height:1.75;margin-top:26px}
.lead-panel p+p{margin-top:18px}
.lead-panel .btn{margin-top:26px;width:112px;height:34px;line-height:34px;font-size:13px}

/* get in touch */
.field{position:absolute;top:2636px;width:226px;height:46px;border:1px solid #ccc;font-size:11px;color:#555;padding:15px 14px}
.signup{position:absolute;left:773px;top:2636px;width:102px;height:46px;line-height:46px}

/* footer */
.site-footer{position:absolute;left:0;top:2750px;width:1200px;height:364px;background:var(--blue);color:var(--white)}
.foot-h{font-size:11px;font-weight:700}
.contact-list{position:absolute;left:135px;top:94px;font-size:11px;line-height:1.5}
.contact-list li{list-style:none;display:flex;gap:16px;margin-bottom:20px}
.foot-menu{position:absolute;left:498px;top:80px;font-size:11px;line-height:1.65}
.foot-menu li{list-style:none}
.foot-brand{position:absolute;left:755px;top:72px;display:flex;align-items:center;gap:14px}
.foot-brand .brand-mark{width:56px;height:56px;background:var(--white)}
.foot-brand .brand-name{color:var(--white);font-size:20px;width:250px}
.follow{position:absolute;left:825px;top:190px;display:flex;align-items:center;gap:14px}
.social{width:42px;height:42px;border-radius:50%}
.foot-rule{position:absolute;left:135px;top:265px;width:930px;height:1px;background:rgba(255,255,255,.45)}
.copyright{position:absolute;left:0;top:312px;width:1200px;text-align:center;font-size:10.5px}
</style>
</head>
<body>

<header class="site-header">
  <div class="brand"><span class="brand-mark"></span><span class="brand-name">Varrowick Biomedical Research Institute</span></div>
  <div class="call">
    <span class="call-icon"><svg width="14" height="14" viewBox="0 0 24 24"><path fill="#fff" d="M6.6 10.8a15 15 0 0 0 6.6 6.6l2.2-2.2c.3-.3.7-.4 1-.2 1.1.4 2.3.6 3.6.6.6 0 1 .4 1 1V20c0 .6-.4 1-1 1A17 17 0 0 1 3 4c0-.6.4-1 1-1h3.5c.6 0 1 .4 1 1 0 1.3.2 2.5.6 3.6.1.3 0 .7-.2 1z"/></svg></span>
    <div><div class="call-label">CALL US</div><div class="call-number">888.888.8888</div></div>
  </div>
  <div class="search">SEARCH<svg width="11" height="11" viewBox="0 0 12 12"><circle cx="5" cy="5" r="3.8" fill="none" stroke="#555" stroke-width="1.4"/><path d="M8 8l3 3" stroke="#555" stroke-width="1.4"/></svg></div>
  <nav class="main-nav">
    <a class="active">HOME</a><a>ABOUT US</a><a>SERVICES</a><a>RESEARCH</a><a>TREATMENT</a><a>TRAINING</a><a>BLOG</a><a>CONTACT US</a>
  </nav>
</header>

<section class="hero" role="img" aria-label="Scientist in a laboratory holding a flask of blue liquid">
  <svg class="hero-arrow" style="left:118px" width="24" height="44" viewBox="0 0 24 44"><path d="M20 4L4 22l16 18" fill="none" stroke="#fff" stroke-width="4"/></svg>
  <svg class="hero-arrow" style="left:1058px" width="24" height="44" viewBox="0 0 24 44"><path d="M4 4l16 18L4 40" fill="none" stroke="#fff" stroke-width="4"/></svg>
  <h1 class="hero-title">NATUROPATHIC<br>TREATMENTS</h1>
  <a class="btn btn-blue">Read More</a>
</section>

<h2 class="sec-title" style="top:678px">OUR SERVICES</h2>
<div class="sec-rule" style="top:716px"></div>

<div class="service" style="left:115px">
  <div class="service-icon"><svg width="44" height="44" viewBox="0 0 44 44"><circle cx="18" cy="18" r="12" fill="none" stroke="#1b6fb4" stroke-width="3"/><path d="M27 27l12 12" stroke="#1b6fb4" stroke-width="4" stroke-linecap="round"/></svg></div>
  <h3>Cutting-edge research</h3>
  <p>There are many variations of passages of Lorem Ipsum av ailable, but the majori ty have suffered alteration</p>
</div>
<div class="service" style="left:365px">
  <div class="service-icon"><svg width="44" height="44" viewBox="0 0 44 44"><circle cx="22" cy="15" r="9" fill="#1b6fb4"/><rect x="18" y="25" width="8" height="5" fill="#1b6fb4"/><path d="M22 30v10M14 36c4 0 8 2 8 4M30 36c-4 0-8 2-8 4" fill="none" stroke="#1b6fb4" stroke-width="2.5"/></svg></div>
  <h3>Innovative Technologies</h3>
  <p>There are many variations of passages of Lorem Ipsum av ailable, but the majori ty have suffered alteration</p>
</div>
<div class="service" style="left:615px">
  <div class="service-icon"><svg width="44" height="44" viewBox="0 0 44 44"><path d="M22 30s-10-6-10-13a5 5 0 0 1 10-1 5 5 0 0 1 10 1c0 7-10 13-10 13z" fill="#1b6fb4"/><path d="M6 22l6 14M38 22l-6 14" stroke="#1b6fb4" stroke-width="3" stroke-linecap="round"/></svg></div>
  <h3>Utilising National</h3>
  <p>There are many variations of passages of Lorem Ipsum av ailable, but the majori ty have suffered alteration</p>
</div>
<div class="service" style="left:865px">
  <div class="service-icon"><svg width="44" height="44" viewBox="0 0 44 44"><circle cx="14" cy="16" r="5" fill="#1b6fb4"/><circle cx="30" cy="16" r="5" fill="#1b6fb4"/><circle cx="22" cy="20" r="6" fill="#1b6fb4"/><path d="M6 32a8 8 0 0 1 16 0zM22 32a8 8 0 0 1 16 0zM12 36a10 10 0 0 1 20 0z" fill="#1b6fb4"/></svg></div>
  <h3>International Partnerships</h3>
  <p>There are many variations of passages of Lorem Ipsum av ailable, but the majori ty have suffered alteration</p>
</div>

<section class="welcome" role="img" aria-label="Researcher in goggles working at a lab bench, tinted blue">
  <h2 class="sec-title" style="top:50px">WELCOME TO OUR SITE</h2>
  <div class="sec-rule" style="top:88px;background:#fff"></div>
  <p class="welcome-text">There are many variations of passages of Lorem Ipsum available, but the majority have suffered alteration in some form, by injected humour, or randomised words which don't look even slightly believable.</p>
  <div class="feature" style="left:240px">
    <svg width="30" height="30" viewBox="0 0 30 30"><path d="M12 3h6v4h-2v8l-2 1V7h-2z" fill="#79b543"/><circle cx="15" cy="18" r="4" fill="none" stroke="#79b543" stroke-width="2.5"/><path d="M5 27h20M9 27c0-3 2-5 4-6" fill="none" stroke="#79b543" stroke-width="2.5"/></svg>
    <h4>BEST RESEARCH</h4><p>There are many variations of pass ages of Lorem Ipsum.</p>
  </div>
  <div class="feature" style="left:488px">
    <svg width="30" height="30" viewBox="0 0 30 30"><circle cx="9" cy="10" r="4" fill="#79b543"/><circle cx="21" cy="10" r="4" fill="#79b543"/><circle cx="15" cy="14" r="4.5" fill="#79b543"/><path d="M3 24a6 6 0 0 1 12 0zM15 24a6 6 0 0 1 12 0zM8 27a7 7 0 0 1 14 0z" fill="#79b543"/></svg>
    <h4>TEAM</h4><p>There are many variations of pass ages of Lorem Ipsum.</p>
  </div>
  <div class="feature" style="left:737px">
    <svg width="30" height="30" viewBox="0 0 30 30"><rect x="3" y="7" width="24" height="17" fill="#79b543"/><path d="M3 7l12 10 12-10" fill="none" stroke="#fff" stroke-width="2"/></svg>
    <h4>CONTACT US</h4><p>There are many variations of pass ages of Lorem Ipsum.</p>
  </div>
  <a class="btn btn-green">Donate Now</a>
</section>

<h2 class="sec-title" style="top:1575px">LATEST BLOG</h2>
<div class="sec-rule" style="top:1613px"></div>

<article class="post" style="left:135px">
  <div class="post-img" role="img" aria-label="Three scientists talking in a laboratory" style="background:linear-gradient(135deg,#e7edf2,#b9c9d8)"></div>
  <div class="post-body"><h4>CONTRARY TO POPULAR BELIEF, LOREM IPSUM IS NOT</h4><p>There are many variations of passages of Lorem Ipsum available, but the majority</p></div>
</article>
<article class="post" style="left:453px">
  <div class="post-img" role="img" aria-label="Researcher examining samples at a lab bench" style="background:linear-gradient(135deg,#dde7f1,#8fb0d2)"></div>
  <div class="post-body"><h4>CONTRARY TO POPULAR BELIEF, LOREM IPSUM IS NOT</h4><p>There are many variations of passages of Lorem Ipsum available, but the majority</p></div>
</article>
<article class="post" style="left:774px">
  <div class="post-img" role="img" aria-label="Scientist holding a petri dish" style="background:linear-gradient(135deg,#d4e0ec,#6f93bd)"></div>
  <div class="post-body"><h4>CONTRARY TO POPULAR BELIEF, LOREM IPSUM IS NOT</h4><p>There are many variations of passages of Lorem Ipsum available, but the majority</p></div>
</article>

<section class="leadership" role="img" aria-label="Three scientists in lab coats reviewing notes together">
  <div class="lead-panel">
    <h3>LEADERSHIP GIVING</h3>
    <p>It is a long established fact that a reader will be distracted by the readable content of a page when looking at its layout. The point of using Lorem Ipsum is that it has a more-or-less normal distribution of letters, as opposed</p>
    <p>The point of using Lorem Ipsum is that it has a more-or-less normal distribution of letters, as opposed</p>
    <a class="btn btn-blue">Read More</a>
  </div>
</section>

<h2 class="sec-title" style="top:2555px">GET IN TOUCH</h2>
<div class="sec-rule" style="top:2593px"></div>
<div class="field" style="left:298px">Name</div>
<div class="field" style="left:537px">E mail ID</div>
<a class="btn btn-green signup">Signup</a>

<footer class="site-footer">
  <div class="foot-h abs" style="left:135px;top:50px">CONTACT US</div>
  <ul class="contact-list">
    <li><svg width="10" height="14" viewBox="0 0 10 14"><path d="M5 0a5 5 0 0 1 5 5c0 4-5 9-5 9S0 9 0 5a5 5 0 0 1 5-5z" fill="#fff"/><circle cx="5" cy="5" r="2" fill="#1b6fb4"/></svg><span>4870 Larkmoor Avenue<br>Dunmere, Florida 30417</span></li>
    <li><svg width="12" height="12" viewBox="0 0 24 24"><path fill="#fff" d="M6.6 10.8a15 15 0 0 0 6.6 6.6l2.2-2.2c.3-.3.7-.4 1-.2 1.1.4 2.3.6 3.6.6.6 0 1 .4 1 1V20c0 .6-.4 1-1 1A17 17 0 0 1 3 4c0-.6.4-1 1-1h3.5c.6 0 1 .4 1 1 0 1.3.2 2.5.6 3.6.1.3 0 .7-.2 1z"/></svg><span>888.888.8888</span></li>
    <li><svg width="12" height="10" viewBox="0 0 12 10"><rect width="12" height="10" fill="#fff"/><path d="M0 0l6 5 6-5" fill="none" stroke="#1b6fb4" stroke-width="1.2"/></svg><span>info@varrowickbr.org</span></li>
  </ul>
  <div class="foot-h abs" style="left:498px;top:50px">MENU</div>
  <ul class="foot-menu">
    <li>HOME</li><li>ABOUT US</li><li>SERVICES</li><li>RESEARCH</li><li>TREATMENT</li><li>TRAINING</li><li>BLOG</li><li>CONTACT US</li>
  </ul>
  <div class="foot-brand"><span class="brand-mark"></span><span class="brand-name">Varrowick Biomedical Research Institute</span></div>
  <div class="follow">
    <span class="foot-h">FOLLOW US</span>
    <span class="social" style="background:#3b5bb0"></span>
    <span class="social" style="background:#29a9e0"></span>
    <span class="social" style="background:#0d3f86"></span>
  </div>
  <div class="foot-rule"></div>
  <div class="copyright">Copyright © 2017 All Rights Reserved</div>
</footer>

</body>
</html>
```